Stationary for Automotive Paintless Dent Repair Company
Panel Soothe LLC
Stationary for Automotive Paintless Dent Repair Company - Automotive
Creative Brief
Modern
Mark Fenley
Owner
478 Birch Ln Allentown, PA 18117
info@PanelSootheLLC.com
www.SmoothMyPanels.com
I would like to see both light and dark examples. I'm open to any kind of design. I prefer a sleek, modern theme to go along with the logo. Linkora, Ravo, and Clipverse logos can also be added.
Logo and/or web address. Open to all suggestions and ideas. Have fun with it!

```html
<!DOCTYPE html>
<html lang="en">
<head>
<meta charset="utf-8">
<title>Panel Soothe LLC – Business Card</title>
<link rel="stylesheet" href="https://fonts.googleapis.com/css2?family=Tinos:wght@400;700&display=swap">
<style>
  :root{
    --page:#e7e9ec;
    --card-white:#ffffff;
    --card-dark:#1c1c1e;
    --blue-deep:#1f5fae;
    --blue-mid:#2f86d6;
    --blue-light:#5fb0ee;
    --grey-band:#8e9196;
    --ink:#3a3b3d;
    --ink-soft:#55575a;
  }
  *{margin:0;padding:0;box-sizing:border-box}
  html,body{width:1200px;height:901px;overflow:hidden}
  body{background:var(--page);font-family:"Tinos",serif;position:relative}

  .card{position:absolute;left:250px;width:700px;height:400px;border-radius:22px;overflow:hidden;
        box-shadow:0 6px 18px rgba(0,0,0,.18)}
  .card--front{top:30px;background:var(--card-white)}
  .card--back{top:471px;background:var(--card-dark)}

  .wave-area{position:absolute;left:0;top:0;width:290px;height:400px;
             background:linear-gradient(160deg,var(--blue-deep) 0%,var(--blue-mid) 60%,var(--blue-light) 100%);
             border-right:6px solid var(--grey-band)}

  .brand{position:absolute;display:flex;align-items:center;gap:10px;white-space:nowrap}
  .brand__dot{width:16px;height:16px;border-radius:50%;background:var(--blue-mid);flex:none}
  .brand__name{font-family:"Tinos",serif;font-weight:700;font-size:30px;letter-spacing:.5px;text-transform:uppercase;color:var(--ink)}
  .card--front .brand{left:345px;top:110px}
  .card--back .brand{left:0;right:0;top:172px;justify-content:center}
  .card--back .brand__name{font-size:36px;letter-spacing:1px;color:var(--blue-light)}

  .person{position:absolute;left:440px;top:200px;text-align:left}
  .person__name{font-size:27px;color:var(--ink);font-weight:400}
  .person__title{font-size:20px;color:var(--ink-soft);margin-top:10px}

  .contact{position:absolute;left:30px;top:150px;list-style:none;color:#fff;font-size:12px;line-height:1.35}
  .contact__item{display:flex;align-items:flex-start;gap:8px;margin-bottom:9px}
  .contact__icon{width:14px;height:14px;flex:none;margin-top:1px}
  .contact__lines{display:flex;flex-direction:column}
</style>
</head>
<body>

<section class="card card--front" aria-label="Business card front">
  <div class="wave-area" role="img" aria-label="Decorative blue and grey wave band"></div>

  <div class="brand">
    <span class="brand__dot"></span>
    <span class="brand__name">Panel Soothe LLC</span>
  </div>

  <div class="person">
    <p class="person__name">Mark Fenley</p>
    <p class="person__title">Owner / C.E.O</p>
  </div>

  <ul class="contact">
    <li class="contact__item">
      <svg class="contact__icon" viewBox="0 0 14 14"><path d="M7 1a4 4 0 0 0-4 4c0 3 4 8 4 8s4-5 4-8a4 4 0 0 0-4-4z" fill="#fff"/><circle cx="7" cy="5" r="1.5" fill="#2f86d6"/></svg>
      <span class="contact__lines"><span>478 Birch Ln</span><span>Allentown, PA 18117</span></span>
    </li>
    <li class="contact__item">
      <svg class="contact__icon" viewBox="0 0 14 14"><path d="M3 1.5l2 0 1 3-1.5 1a7 7 0 0 0 4 4l1-1.5 3 1v2a1.5 1.5 0 0 1-1.5 1.5A10 10 0 0 1 1.5 3 1.5 1.5 0 0 1 3 1.5z" fill="#fff"/></svg>
      <span class="contact__lines"><span>610-555-0142</span><span>610-555-0187</span><span>610-555-0119</span></span>
    </li>
    <li class="contact__item">
      <svg class="contact__icon" viewBox="0 0 14 14"><rect x="1" y="3" width="12" height="8" rx="1" fill="#fff"/><path d="M1.5 3.5L7 8l5.5-4.5" stroke="#2f86d6" stroke-width="1" fill="none"/></svg>
      <span class="contact__lines"><span>info@PanelSootheLLC.com</span></span>
    </li>
    <li class="contact__item">
      <svg class="contact__icon" viewBox="0 0 14 14"><circle cx="7" cy="7" r="5.5" fill="none" stroke="#fff" stroke-width="1.2"/><ellipse cx="7" cy="7" rx="2.3" ry="5.5" fill="none" stroke="#fff" stroke-width="1"/><path d="M1.5 7h11" stroke="#fff" stroke-width="1"/></svg>
      <span class="contact__lines"><span>www.SmoothMyPanels.com</span></span>
    </li>
  </ul>
</section>

<section class="card card--back" aria-label="Business card back">
  <div class="brand">
    <span class="brand__dot"></span>
    <span class="brand__name">Panel Soothe LLC</span>
  </div>
</section>

</body>
</html>
```